Dalvorn-Ke Photography needs a poster for a upcoming event

We need a Music Concert Poster designed for a musician named Marc T. Lindow. The concert is happening 6:30 pm, Saturday, January 10, 2015 Look to our current design ideas for inspiration. Keep it clean and simple but I want to see your creative ideas. Please view the throw togethers screenshots I have included in this project and then use one of the clean images in your design. Visit www.pinboardia.example/marclind/concert-posters/ for the musicians favorite music posters and gather ideas from there as well.

Industry/Entity Type

Event

Requirements
Nice to have
• Lets tend to lean towards a more sanserif font

```html
<!DOCTYPE html>
<html lang="en">
<head>
<meta charset="utf-8">
<title>Marc T. Lindow in Concert</title>
<link rel="stylesheet" href="https://fonts.googleapis.com/css2?family=Poppins:wght@600&family=Questrial&family=Arimo:wght@400;700&display=swap">
<style>
  :root {
    --paper: #ffffff;
    --ink: #050505;
    --gold: #c2a84d;
    --white: #ffffff;
    --band: rgba(90, 90, 90, 0.55);
    --glow: #5a5a5a;
    --photo-top: #3b2c26;
    --photo-bottom: #4b2468;
  }
  * { margin: 0; padding: 0; box-sizing: border-box; }
  html, body {
    width: 746px; height: 1200px; overflow: hidden;
    background: var(--paper);
  }
  .poster {
    position: absolute; left: 25px; top: 24px;
    width: 697px; height: 1149px;
    background: radial-gradient(ellipse 340px 420px at 190px 640px, var(--glow) 0%, #2a2a2a 45%, var(--ink) 80%);
    overflow: hidden;
  }
  .flourish {
    position: absolute; left: 177px; top: 36px; width: 330px; height: 66px;
    background: linear-gradient(90deg, transparent 0%, rgba(194,168,77,0.35) 30%, rgba(194,168,77,0.35) 70%, transparent 100%);
    border-radius: 33px;
  }
  .artist {
    position: absolute; left: 0; top: 116px; width: 100%;
    text-align: center; color: var(--gold);
    font-family: "Poppins", sans-serif; font-weight: 600;
    font-size: 64px; letter-spacing: 2px; line-height: 1;
  }
  .subtitle {
    position: absolute; left: 0; top: 214px; width: 100%;
    text-align: center; color: var(--white);
    font-family: "Questrial", sans-serif; font-size: 34px;
    letter-spacing: 30px; padding-left: 30px; line-height: 1;
  }
  .divider { position: absolute; left: 145px; top: 280px; width: 390px; height: 24px; }
  .portrait {
    position: absolute; left: 75px; top: 336px; width: 622px; height: 603px;
    background: linear-gradient(180deg, var(--photo-top) 0%, var(--photo-bottom) 100%);
    border-radius: 180px 180px 0 0;
  }
  .date-band {
    position: absolute; left: 0; top: 940px; width: 100%; height: 38px;
    background: var(--band);
    text-align: center; color: var(--gold);
    font-family: "Arimo", sans-serif; font-size: 25px; line-height: 38px;
  }
  .venue {
    position: absolute; left: 0; top: 998px; width: 100%;
    text-align: center; color: var(--white);
    font-family: "Arimo", sans-serif; font-size: 18px; line-height: 35px;
    letter-spacing: 0.4px;
  }
  .entry {
    position: absolute; left: 0; top: 1088px; width: 100%;
    text-align: center; color: var(--gold);
    font-family: "Poppins", sans-serif; font-weight: 600;
    font-size: 26px; letter-spacing: 1.5px; line-height: 1.3;
  }
</style>
</head>
<body>
  <main class="poster">
    <div class="flourish" role="img" aria-label="Gold calligraphic flourish ornament"></div>
    <h1 class="artist">MARC T. LINDOW</h1>
    <p class="subtitle">IN CONCERT</p>
    <svg class="divider" viewBox="0 0 390 24" aria-hidden="true">
      <line x1="0" y1="12" x2="150" y2="12" stroke="#c2a84d" stroke-width="2"/>
      <line x1="240" y1="12" x2="390" y2="12" stroke="#c2a84d" stroke-width="2"/>
      <circle cx="70" cy="12" r="3" fill="#c2a84d"/>
      <circle cx="320" cy="12" r="3" fill="#c2a84d"/>
      <rect x="155" y="2" width="80" height="20" rx="10" fill="#c2a84d" opacity="0.35"/>
    </svg>
    <div class="portrait" role="img" aria-label="Photo of the musician in a purple shirt holding an acoustic guitar over his shoulder"></div>
    <div class="date-band">January 10, 2015, Saturday,&nbsp; 6:30 pm</div>
    <p class="venue">Harbor Grove SDA Church,<br>482 Linden Crest Ave, Harbor Grove, FL- 32590</p>
    <p class="entry">FREE ENTRY</p>
  </main>
</body>
</html>
```